Verdant Pathworks Business Card

want the back of card to be blue- with the logo in the center
front of card- info plus logo (info being mailing address, email address, and website address )
4 different names with titles to have on cards
1) Dominic Ashvale - Owner
2) Bethany Korvuth- Customer Relationship Specialist
3) Luca Brennwick- Vice President of Sales
4) Neil Umbright- Chief Technology Officer

Target Market(s)

tech company in the government/probation office industry

Industry/Entity Type

Government Office

Contact Information for Business Card

1) Dominic Ashvale - Owner

Colors
0355a3
ffffff

Requirements
Must have
• back side should be blue, with the logo placed in the center
• front side needs to include both the logo, as well as company info (info should include website address, email address, and mailing address)

```html
<!DOCTYPE html>
<html lang="en">
<head>
<meta charset="UTF-8">
<title>Verdant Pathworks Business Card</title>
<link href="https://fonts.googleapis.com/css2?family=Crimson+Text:wght@600&family=Roboto:wght@400&display=swap" rel="stylesheet">
<style>
  :root {
    --brand-blue: #0355a3;
    --white: #ffffff;
    --grey-text: #6e6e6e;
    --body-text: #4a4a4a;
    --grey-band: #7d7d80;
    --backdrop: #ececec;
  }
  * { margin: 0; padding: 0; box-sizing: border-box; }
  html, body {
    width: 1125px; height: 1200px; overflow: hidden;
    background: var(--backdrop);
  }
  .card {
    position: absolute; left: 171px;
    width: 826px; height: 472px;
    overflow: hidden;
  }
  .card-front { top: 106px; background: var(--white); }
  .card-back { top: 640px; background: var(--brand-blue); }

  .wordmark {
    font-family: "Crimson Text", Georgia, serif;
    font-weight: 600;
    text-align: center;
    line-height: 1.02;
    letter-spacing: 1px;
    text-transform: uppercase;
  }
  .card-front .wordmark {
    position: absolute; left: 470px; top: 95px; width: 310px;
    font-size: 44px; color: var(--brand-blue);
  }
  .card-back .wordmark {
    position: absolute; left: 0; right: 0; top: 150px;
    font-size: 58px; color: var(--white);
  }

  .holder-name {
    position: absolute; left: 57px; top: 256px;
    font-family: "Crimson Text", Georgia, serif; font-weight: 600;
    font-size: 34px; color: var(--brand-blue); line-height: 1;
  }
  .holder-title {
    position: absolute; left: 57px; top: 295px;
    font-family: "Roboto", Arial, sans-serif;
    font-size: 20px; color: var(--grey-text);
  }
  .contact-list {
    position: absolute; left: 57px; top: 334px; list-style: none;
    font-family: "Roboto", Arial, sans-serif;
    font-size: 19px; color: var(--body-text);
  }
  .contact-list li { display: flex; align-items: center; height: 27px; white-space: nowrap; }
  .contact-list svg { width: 18px; height: 18px; margin-right: 12px; fill: var(--brand-blue); flex: none; }

  .footer-band {
    position: absolute; left: 0; bottom: 0; width: 470px; height: 15px;
    background: var(--grey-band);
  }
  .web-band {
    position: absolute; right: 0; bottom: 0; width: 352px; height: 36px;
    background: var(--brand-blue);
    clip-path: polygon(38px 0, 100% 0, 100% 100%, 0 100%);
    font-family: "Roboto", Arial, sans-serif; font-size: 19px;
    color: var(--white);
    display: flex; align-items: center; padding-left: 42px;
  }
  .back-web {
    position: absolute; left: 0; right: 0; top: 393px;
    text-align: center;
    font-family: "Roboto", Arial, sans-serif; font-size: 19px;
    letter-spacing: 3px; color: var(--white);
  }
</style>
</head>
<body>
  <section class="card card-front">
    <div class="wordmark">Verdant<br>Pathworks</div>
    <div class="holder-name">Dominic Ashvale</div>
    <div class="holder-title">Owner</div>
    <ul class="contact-list">
      <li><svg viewBox="0 0 24 24"><path d="M6.6 10.8a15.1 15.1 0 0 0 6.6 6.6l2.2-2.2c.3-.3.7-.4 1-.2 1.1.4 2.3.6 3.6.6.6 0 1 .4 1 1V20c0 .6-.4 1-1 1A17 17 0 0 1 3 4c0-.6.4-1 1-1h3.5c.6 0 1 .4 1 1 0 1.3.2 2.5.6 3.6.1.3 0 .7-.2 1z"/></svg>555-214-7730</li>
      <li><svg viewBox="0 0 24 24"><path d="M7 1h10a2 2 0 0 1 2 2v18a2 2 0 0 1-2 2H7a2 2 0 0 1-2-2V3a2 2 0 0 1 2-2zm0 3v14h10V4zm5 15.5a1 1 0 1 0 0 2 1 1 0 0 0 0-2z"/></svg>555-418-2096</li>
      <li><svg viewBox="0 0 24 24"><path d="M2 6h20v12H2zm2 2v.3l8 5 8-5V8l-8 5z"/></svg>info@verdantpathworks.com</li>
      <li><svg viewBox="0 0 24 24"><path d="M12 2a7 7 0 0 0-7 7c0 5.2 7 13 7 13s7-7.8 7-13a7 7 0 0 0-7-7zm0 9.5A2.5 2.5 0 1 1 12 6.5a2.5 2.5 0 0 1 0 5z"/></svg>1420 Harlow St, Ridgeford, OR 97301</li>
    </ul>
    <div class="footer-band"></div>
    <div class="web-band">www.verdantpathworks.com</div>
  </section>

  <section class="card card-back">
    <div class="wordmark">Verdant<br>Pathworks</div>
    <div class="back-web">www.verdantpathworks.com</div>
  </section>
</body>
</html>
```